Curbside Bin Butler Valet Trash Recycling

I want to create a colorful brochure, I really like my company colors, with basic information about valet trash for apartment complexes. You can include some apartment recycling information as well, but 80% trash, 20% recycling. I have included my logo in the attachments. Also, you can find information at curbsidebinbutler.example, very basic and I will be redoing my website as well.

many people are giving information about business and residential recycling, I only want information on trash and recycling valet for apartments

Target Market(s)

apartment complex tenants and management

Industry/Entity Type

Apartment

Number of Pages Required

4 page

Font styles to use
Serif
Sans Serif

Colors
9bcb3b
f37122
0355a3

Requirements
Must have
• Tri-Fold brochure, colorful, well organized. Advantages for tenants and for property management.

```html
<!DOCTYPE html>
<html lang="en">
<head>
<meta charset="utf-8">
<title>Curbside Bin Butler – Tri-Fold Brochure</title>
<link href="https://fonts.googleapis.com/css2?family=Lato:wght@400;700;900&family=Lora:wght@400;700&display=swap" rel="stylesheet">
<style>
  :root{
    --green:#8cc63f;
    --green-deep:#9bcb3b;
    --orange:#f37122;
    --blue:#0355a3;
    --blue-mid:#1f4fa8;
    --white:#ffffff;
    --ink:#111111;
    --stage:#d9d9d9;
    --photo-light:#d8d8d8;
    --photo-dark:#6e6e6e;
  }
  *{box-sizing:border-box;margin:0;padding:0}
  html,body{width:1200px;height:900px;overflow:hidden}
  body{background:var(--stage);font-family:"Lato",Arial,sans-serif;position:relative}

  .brochure{position:absolute;left:60px;top:70px;width:1080px;height:760px;display:flex;box-shadow:0 6px 20px rgba(0,0,0,.25)}
  .panel{position:relative;width:360px;height:760px;overflow:hidden}
  .panel-bg{position:absolute;inset:0;width:100%;height:100%}

  /* Left panel */
  .tag{position:absolute;left:0;height:30px;padding:0 22px 0 28px;border-radius:0 16px 16px 0;font-family:"Lora",Georgia,serif;font-size:18px;color:var(--white);display:flex;align-items:center}
  .tag-about{top:54px;background:var(--green)}
  .tag-services{top:508px;background:var(--blue-mid)}
  .about-copy{position:absolute;left:34px;top:98px;width:300px;color:var(--white);font-size:11.6px;font-weight:700;line-height:1.32}
  .about-copy p{margin-bottom:13px}
  .services-copy{position:absolute;left:36px;top:548px;width:304px;color:var(--blue-mid);font-size:11.4px;font-weight:700;line-height:1.35;text-align:justify}
  .services-copy p{margin-bottom:10px}
  .services-copy .tagline{text-align:left}
  .footer-url{position:absolute;top:714px;font-size:14px;font-weight:700;color:var(--blue-mid);letter-spacing:.2px}
  .footer-url.left{left:46px}
  .footer-url.right{right:22px}

  /* Middle panel */
  .panel-middle{background:var(--orange)}
  .wordmark{position:absolute;display:flex;align-items:center;gap:8px;font-family:"Lato",Arial,sans-serif;font-weight:700;font-size:22px;white-space:nowrap}
  .wordmark .dot{width:22px;height:22px;border-radius:50%}
  .wordmark-sub{position:absolute;font-size:11px;font-weight:400;white-space:nowrap}
  .panel-middle .wordmark{left:24px;top:56px;color:var(--white)}
  .panel-middle .wordmark .dot{background:var(--white)}
  .panel-middle .wordmark-sub{left:54px;top:86px;color:var(--white)}

  .contact-card{position:absolute;left:42px;top:144px;width:268px;height:386px;background:var(--green);border:3px solid var(--blue-mid)}
  .contact-name{position:absolute;left:0;right:0;top:18px;text-align:center;font-family:"Lora",Georgia,serif;font-size:25px;color:var(--white)}
  .contact-name::after{content:"";display:block;width:104px;height:2px;background:var(--blue-mid);margin:3px auto 0}
  .contact-list{position:absolute;left:20px;top:76px;list-style:none;color:var(--ink);font-size:13px}
  .contact-list li{display:flex;gap:8px;align-items:flex-start;margin-bottom:10px;line-height:1.2}
  .contact-list svg{flex:none;width:18px;height:16px;margin-top:1px}
  .call-label{position:absolute;left:86px;top:222px;width:94px;height:24px;background:var(--blue-mid);color:var(--white);font-family:"Lora",Georgia,serif;font-weight:700;font-size:14px;display:flex;align-items:center;justify-content:center}
  .call-number{position:absolute;left:0;right:0;top:250px;text-align:center;font-family:"Lora",Georgia,serif;font-weight:700;font-size:26px;color:var(--ink)}
  .partner-badge{position:absolute;left:58px;top:296px;width:152px;height:104px;background:var(--white);border-radius:8px;border:2px solid #e9e9e9}
  .partner-badge::after{content:"";position:absolute;left:12px;right:12px;top:12px;bottom:12px;background:var(--green-deep);border-radius:4px}
  .partner-note{position:absolute;left:0;right:0;top:348px;text-align:center;font-size:14px;color:var(--blue-mid)}
  .mid-mark{position:absolute;left:0;right:0;top:630px;display:flex;justify-content:center;gap:10px;align-items:center;color:var(--white);font-weight:700;font-size:20px}
  .mid-mark .dot{width:24px;height:24px;border-radius:50%;background:var(--white)}

  /* Right panel */
  .panel-right .wordmark{left:34px;top:52px;color:var(--blue-mid)}
  .panel-right .wordmark .dot{background:var(--green)}
  .panel-right .wordmark-sub{left:64px;top:82px;color:var(--orange)}
  .photo{position:absolute;left:0;top:112px;width:360px;height:380px;background:linear-gradient(160deg,var(--photo-light),var(--photo-dark))}
  .city{position:absolute;left:0;right:0;top:526px;text-align:center;font-size:24px;font-weight:900;color:var(--white)}
  .pitch{position:absolute;left:40px;right:30px;top:562px;text-align:center;font-size:13.4px;font-weight:700;line-height:1.34;color:var(--blue-mid)}
</style>
</head>
<body>
<main class="brochure">

  <!-- Inside left: about & services -->
  <section class="panel panel-left">
    <svg class="panel-bg" viewBox="0 0 360 760" preserveAspectRatio="none" aria-hidden="true">
      <rect width="360" height="760" fill="#ffffff"/>
      <path d="M0 0 H250 C300 0 330 20 360 40 V420 C300 380 220 380 150 410 C90 440 40 440 0 420 Z" fill="#1f4fa8"/>
      <path d="M0 420 C40 440 90 440 150 410 C220 380 300 380 360 420 V430 C300 395 220 395 152 424 C92 452 40 452 0 432 Z" fill="#f37122"/>
      <path d="M0 470 C80 480 150 468 230 450 C290 438 330 440 360 448 V760 H0 Z" fill="#8cc63f"/>
      <path d="M0 662 C120 668 240 680 360 700 V760 H0 Z" fill="#1f4fa8"/>
      <path d="M0 672 C120 680 240 692 360 712 V760 H0 Z" fill="#ffffff"/>
    </svg>
    <h2 class="tag tag-about">About The Company</h2>
    <div class="about-copy">
      <p>Curbside Bin Butler (CBB) is a Houston-based business created by Marcus Delane, a Bayou State College student and professional mixed martial artist. Marcus previously owned and operated the successful trash removal service, Marcus's Haul-Away, while he was a high school student-athlete in Galveston. He has now founded a similar service in the Houston area.</p>
      <p>Marcus plans to keep CBB ahead of its competitors by focusing on customer satisfaction, technology, efficiency, and professionalism</p>
      <p>CBB is fully ensured; proof of insurance will be provided upon request</p>
      <p>Testimonials from former clients reveal so much about how a company operates and performs. We are happy to provide references upon request.</p>
    </div>
    <h2 class="tag tag-services">CBB Services</h2>
    <div class="services-copy">
      <p>Curbside Bin Butler (CBB) is a complete trash and recycling valet service designed to keep apartment complexes and its units clean, make complexes more environmentally friendly, and to keep tenants satisfied</p>
      <p class="tagline">Keeping Apartment Complexes Cleaner and Greener Across Houston.</p>
    </div>
    <p class="footer-url left">www.curbsidebinbutler.example</p>
  </section>

  <!-- Back middle: contact -->
  <section class="panel panel-middle">
    <svg class="panel-bg" viewBox="0 0 360 760" preserveAspectRatio="none" aria-hidden="true">
      <path d="M0 722 L180 760 L360 722 V760 H0 Z" fill="#1f4fa8"/>
    </svg>
    <div class="wordmark"><span class="dot"></span>Curbside Bin Butler</div>
    <p class="wordmark-sub">curbsidebinbutler.example</p>

    <div class="contact-card">
      <h1 class="contact-name">Marcus Delane</h1>
      <ul class="contact-list">
        <li><svg viewBox="0 0 18 16"><path d="M9 1 L17 8 H14.5 V15 H10.5 V10 H7.5 V15 H3.5 V8 H1 Z" fill="#1f4fa8"/></svg><span>2840 Magnolia Ave #212<br>Ridgeview, TX 77000</span></li>
        <li><svg viewBox="0 0 18 16"><rect x="1" y="3" width="16" height="11" fill="#1f4fa8"/><path d="M1 3 L9 9 L17 3" stroke="#8cc63f" stroke-width="1.4" fill="none"/></svg><span>hello@curbsidebinbutler.example</span></li>
        <li><svg viewBox="0 0 18 16"><circle cx="9" cy="8" r="7" fill="none" stroke="#1f4fa8" stroke-width="1.4"/><ellipse cx="9" cy="8" rx="3" ry="7" fill="none" stroke="#1f4fa8" stroke-width="1.2"/><path d="M2 8 H16 M3 4.5 H15 M3 11.5 H15" stroke="#1f4fa8" stroke-width="1.1"/></svg><span>curbsidebinbutler.example</span></li>
      </ul>
      <p class="call-label">CALL US:</p>
      <p class="call-number">409-555-0147</p>
      <div class="partner-badge" role="img" aria-label="Partner badge"></div>
      <p class="partner-note" style="top:402px">CBB is partnered with</p>
    </div>

    <div class="mid-mark"><span class="dot"></span>Curbside Bin Butler</div>
  </section>

  <!-- Front cover -->
  <section class="panel panel-right">
    <svg class="panel-bg" viewBox="0 0 360 760" preserveAspectRatio="none" aria-hidden="true">
      <rect width="360" height="760" fill="#ffffff"/>
    </svg>
    <div class="wordmark"><span class="dot"></span>Curbside Bin Butler</div>
    <p class="wordmark-sub">curbsidebinbutler.example</p>
    <div class="photo" role="img" aria-label="Black and white photo of a person carrying a bag of trash in a recycling bin"></div>
    <svg class="panel-bg" viewBox="0 0 360 760" preserveAspectRatio="none" aria-hidden="true">
      <path d="M0 100 C90 112 200 116 360 96 V112 C220 128 100 130 0 128 Z" fill="#1f4fa8"/>
      <path d="M0 440 C90 470 230 480 360 440 V470 C250 480 150 500 60 520 L0 530 Z" fill="#1f4fa8"/>
      <path d="M0 480 C110 470 250 440 360 446 V460 C250 458 130 486 0 500 Z" fill="#f37122"/>
      <path d="M0 500 C130 486 250 458 360 460 V686 H0 Z" fill="#8cc63f"/>
      <path d="M0 700 C120 694 240 680 360 668 V690 C240 700 120 712 0 716 Z" fill="#1f4fa8"/>
    </svg>
    <h2 class="city">HOUSTON, TEXAS</h2>
    <p class="pitch">Taking out somebody's trash is a timeless gesture of kindness. Curbside Bin Butler (CBB) takes that act of kindness one step further: your tenants will never again have to bother with trash past their own doorsteps!</p>
    <p class="footer-url right">www.curbsidebinbutler.example</p>
  </section>

</main>
</body>
</html>
```